Lantern over the Harbor ~ A Widening Passage for Writers

My book is called “Lantern over the Harbor.” Its subtitle is “A Widening Passage for Writers.” It is a book about being a poet, writing poetry, and the ways in which poets are connected to both society and the central energy of the Universe. I want the cover design to be abstract and impressionistic. A suggestion of fireworks or a starburst would be a plus. To be consistent with the 3 other books I have published, I want the font for the title, as well as my name (Dorothea Quillbrake) to be Papyrus. The subtitle font can be something more plain and sans serif, like Arial or Franklin Gothic Book, probably in italics. As for color, I definitely want pale gold (angelic). Possible other complimentary colors could be either light or dark shades of gray, turquoise, rose, rust or red. I'm attaching the back cover text and also three pages from inside the book that have line drawings, to give an example of the interior artwork.
Updates

Forgot to mention: My book is a paperback. Its size will be 8.5" high and 5.5" wide. I'm self-publishing it, and it will be printed by Halvern Printworks in Nebraska, USA. It has 104 pages. I think you need the number of pages, in order to make the spine of the book the correct width.

Target Market(s)

My target market is people who write poetry or are interested in how poetry is written.

Industry/Entity Type

Poetry

Font styles to use
Sans Serif
Other font styles liked:
• Papyrus for the front cover. Arial or another sans serif font on the back cover.

Colors

Designer to choose colors to be used in the design.

Requirements
Must have
• My book cover needs to be inspiring and uplifting, as well as abstract and impressionistic, with kind of a "New Age" feel. I don't want anything that looks rigid and scholarly.
Nice to have
• The book talks about the connection poets have to the Universe and the Creative Energy at the center of everything. The cover should convey that Energy.
Should not have
• My cover should not be realistic, logical or straight-laced. I want something that feels free, imaginative and unfettered.

```html
<!DOCTYPE html>
<html lang="en">
<head>
<meta charset="utf-8">
<title>Lantern over the Harbor – Cover Wrap</title>
<link href="https://fonts.googleapis.com/css2?family=Macondo&family=Gelasio:ital,wght@0,400;0,700;1,700&family=Arimo&display=swap" rel="stylesheet">
<style>
  :root{
    --page:#ffffff;
    --ink-light:#fbf3e4;
    --spine-gold:#f2d9a2;
    --title-brown:#3a2412;
    --teal-dark:#2d4d5c;
    --teal:#5f8c91;
    --rust:#8a3f1c;
    --ember:#c4641f;
    --gold:#f4c25a;
    --pale-gold:#f8e4a8;
    --photo-tone:#b9a58f;
  }
  *{margin:0;padding:0;box-sizing:border-box}
  html,body{width:1200px;height:821px;overflow:hidden;background:var(--page)}
  .canvas{position:relative;width:1200px;height:821px;background:var(--page)}
  .wrap{position:absolute;left:63px;top:63px;width:1074px;height:695px;overflow:hidden}
  .wrap-art{position:absolute;inset:0;
    background:
      radial-gradient(ellipse 190px 210px at 815px 350px, rgba(255,246,200,.95), rgba(250,205,110,.75) 45%, rgba(244,180,90,0) 100%),
      radial-gradient(ellipse 330px 380px at 815px 350px, rgba(246,190,95,.8), rgba(240,170,90,0) 100%),
      radial-gradient(ellipse 260px 200px at 1040px 40px, rgba(110,150,150,.55), rgba(110,150,150,0) 100%),
      radial-gradient(ellipse 180px 260px at 600px 620px, rgba(120,160,170,.45), rgba(120,160,170,0) 100%),
      linear-gradient(90deg, rgba(0,0,0,0) 0, rgba(0,0,0,0) 560px, rgba(240,200,130,.9) 620px, rgba(238,196,130,.95) 100%),
      radial-gradient(ellipse 380px 300px at 120px 80px, var(--teal-dark), rgba(45,77,92,0) 100%),
      radial-gradient(ellipse 360px 320px at 420px 120px, #4f7d86, rgba(79,125,134,0) 100%),
      radial-gradient(ellipse 420px 360px at 300px 620px, var(--ember), rgba(196,100,31,0) 100%),
      linear-gradient(180deg, #3c5a66 0%, #6a6660 38%, #a0522a 68%, var(--rust) 100%);
  }
  .back-copy{position:absolute;left:0;top:0;width:565px;color:var(--ink-light);
    font-family:"Gelasio",Georgia,serif;font-size:14.6px;line-height:17.3px;text-align:center}
  .back-copy p{position:absolute;left:38px;width:490px}
  .back-copy em{font-style:italic;font-weight:700;font-size:17px}
  .intro{top:68px}
  .summary{top:157px}
  .chapters{top:282px}
  .career{top:351px}
  .author-photo{position:absolute;left:38px;top:507px;width:59px;height:87px;
    background:linear-gradient(160deg,#d8cfc4,var(--photo-tone) 60%,#6f8a5a)}
  .praise{position:absolute;left:108px;top:505px;width:400px;text-align:left;color:var(--ink-light);
    font-family:"Gelasio",Georgia,serif;font-size:14.6px;line-height:17.3px}
  .isbn-box{position:absolute;left:302px;top:609px;width:134px;height:56px;background:#fdfbfa}
  .spine{position:absolute;left:520px;top:0;width:58px;height:695px;color:var(--spine-gold);
    font-family:"Macondo",fantasy;writing-mode:vertical-rl}
  .spine-title{position:absolute;left:10px;top:88px;font-size:27px;line-height:30px;white-space:nowrap}
  .spine-title small{font-size:15px}
  .spine-author{position:absolute;left:12px;top:437px;font-size:25px;line-height:28px;white-space:nowrap}
  .front{position:absolute;left:578px;top:0;width:496px;height:695px;color:var(--title-brown);text-align:center}
  .title{font-family:"Macondo",fantasy;font-weight:400;position:absolute;left:0;right:0;top:60px}
  .title-line{display:block;line-height:86px}
  .title .big{font-size:88px}
  .title .small{font-size:40px}
  .subtitle{position:absolute;left:0;right:0;top:232px;font-family:"Arimo",Arial,sans-serif;font-size:23px}
  .author{position:absolute;left:0;right:0;top:590px;font-family:"Macondo",fantasy;font-size:42px}
</style>
</head>
<body>
<div class="canvas">
  <div class="wrap">
    <div class="wrap-art" role="img" aria-label="Impressionistic painted background: deep teal and rust on the back cover, a radiant pale gold starburst on the front"></div>

    <div class="back-copy">
      <p class="intro"><em>Lantern over the Harbor</em> is indeed “A Widening Passage for Writers.” It is written by Dorothea Quillbrake, an exciting, imaginative voice in American poetry.</p>
      <p class="summary">In <em>Lantern over the Harbor,</em> Dorothea discusses the essential elements of poetry and the process of writing it. She offers an inspiring view of the mission of poets and their connection to both society and the larger forces in the Universe. Her book is motivational, refreshing and irrepressibly optimistic</p>
      <p class="chapters">The seven intriguing chapters in Lantern over the Harbor are LIBERATION ~ EXPERIENCE ~ WORDS ~ POETRY ~ INTEGRITY ~ BEAUTY ~ CREATION</p>
      <p class="career">For over 50 years, Dorothea has been a teacher of writing and poetry. Since 2007, she has published three books of her poems: Salt on the Windowsill, The Amber Edge of Morning and The Quiet Copper Sea. Her work overflows with her characteristically rich images and quirky metaphors. It runs the gamut from subtle eroticism to abject grief, from defiant rage to philosophical meditation, and from borderline blasphemy to lyrical fantasy.</p>
    </div>

    <div class="author-photo" role="img" aria-label="Author portrait photograph"></div>
    <p class="praise">Dorothea has been called by critic Russell Tamberlane “a poet to bereckoned with; bright, feisty, compassionate.” (The Valley Courier, Ashbury, PA). Author Lorna Vetchley (“Hollowmere,” 2011) says Dorothea’s poetry is like “a perpetual Surprise Party ~ memorable, insightful and thematically fascinating.”</p>
    <div class="isbn-box"></div>

    <div class="spine">
      <span class="spine-title">Lantern <small>over the</small> Harbor</span>
      <span class="spine-author">Dorothea Quillbrake</span>
    </div>

    <div class="front">
      <h1 class="title">
        <span class="title-line"><span class="big">Lantern</span> <span class="small">over</span></span>
        <span class="title-line"><span class="small">the</span> <span class="big">Harbor</span></span>
      </h1>
      <p class="subtitle">A Widening Passage for Writers</p>
      <p class="author">Dorothea Quillbrake</p>
    </div>
  </div>
</div>
</body>
</html>
```